Energy Healing for pregnant women postcard

I am an intuitive energy healer specializing in the care of pregnant women and their babies. I have an existing logo that is attached that should be placed on the card,sizing is at your discretion, recolor as needed. The message of the card should be one that conveys tranquility, growth, life and light. Images of pregnancy and motherhood could also fit well on the card, but that is not required if the preceding messages can be conveyed through other imagery. Also on the card, the following should appear: (company name and tag line)Positivity & JoyHealing the mind, body, spirit and soul with Energy provided to all living things by the Universe. Space should be left for my name and credentials on the front, while the address space on the back will be used for more contact information. Opposite the address block on the back, please leave room for a text box that will include benefits of the services. About 2"x3" should suffice.

Target Market(s)

Pregnant women and newly post-partum women

Industry/Entity Type

Health And Wellness

Font styles to use
Script

Colors
b05ba4
b768aa
d3a5cc
ecdaeb
e7f5f8
cfdeed
cee9f5
85cae6

Requirements
Must have
• Company logo. Company name. Tag line. Individual name and certifications
Nice to have
• Pictures or images that convey peace, tranquility healing and growth.
Should not have
• Anything harsh.

```html
<!DOCTYPE html>
<html lang="en">
<head>
<meta charset="utf-8">
<title>Harbor &amp; Fern – Energy Healing Postcard</title>
<link rel="stylesheet" href="https://fonts.googleapis.com/css2?family=Dancing+Script:wght@500;600&family=Fira+Sans+Condensed:wght@400;600&family=PT+Sans:wght@400;700&family=Roboto+Condensed:wght@300;400&display=swap">
<style>
  :root {
    --orchid: #b05ba4;
    --orchid-soft: #b768aa;
    --lilac: #d3a5cc;
    --blush: #ecdaeb;
    --mist: #e7f5f8;
    --sky-pale: #cee9f5;
    --sky: #85cae6;
    --leaf: #a9c79a;
    --ink: #3b4a5a;
    --body-ink: #3a3a3a;
    --backdrop: #efe9e1;
    --white: #ffffff;
  }
  * { box-sizing: border-box; margin: 0; padding: 0; }
  html, body { width: 1200px; height: 500px; overflow: hidden; }
  body { background: var(--backdrop); position: relative; font-family: "PT Sans", sans-serif; }

  .postcard { position: absolute; top: 33px; width: 558px; height: 433px; overflow: hidden; box-shadow: 0 2px 6px rgba(0,0,0,.25); }
  .postcard--front { left: 27px; }
  .postcard--back { left: 609px; background: var(--white); }

  /* Front */
  .front__photo { position: absolute; inset: 0;
    background:
      radial-gradient(ellipse 60% 40% at 45% 62%, #8fb0c9 0%, rgba(143,176,201,0) 70%),
      linear-gradient(180deg, #1f2f1c 0%, #2f4a26 25%, #5f8a3c 55%, #86ad58 75%, #9cbf6a 100%); }
  .front__wave { position: absolute; inset: 0; }
  .front__tagline { position: absolute; left: 34px; top: 10px; width: 400px;
    font-family: "Dancing Script", cursive; font-weight: 500; font-size: 24px; line-height: 31px; color: var(--white); }
  .brand { position: absolute; left: 398px; top: 92px; display: flex; align-items: center; gap: 8px;
    font-family: "Dancing Script", cursive; font-weight: 600; font-size: 26px; color: var(--mist); }
  .brand__dot { width: 12px; height: 12px; border-radius: 50%; background: var(--mist); }
  .practitioner { position: absolute; left: 34px; top: 346px; color: var(--white); }
  .practitioner__name { font-family: "Dancing Script", cursive; font-weight: 600; font-size: 25px; line-height: 30px; }
  .practitioner__title { font-size: 15px; line-height: 18px; }
  .benefits { position: absolute; left: 300px; top: 292px; list-style: none; color: var(--white); font-size: 13.5px; line-height: 16.6px; }
  .benefits li { position: relative; padding-left: 13px; }
  .benefits li::before { content: ""; position: absolute; left: 0; top: 5px; width: 7px; height: 7px; border-radius: 50%; background: var(--white); }

  /* Back */
  .back__wash { position: absolute; left: 0; top: 0; width: 330px; height: 357px;
    background: linear-gradient(90deg, var(--sky-pale) 0%, var(--mist) 45%, rgba(255,255,255,0) 100%); }
  .info { position: absolute; left: 25px; top: 18px; width: 270px; }
  .info__heading { font-family: "Fira Sans Condensed", sans-serif; font-weight: 600; font-size: 17.5px; line-height: 20px; color: var(--ink); margin-bottom: 7px; }
  .info__text { font-family: "Roboto Condensed", sans-serif; font-weight: 400; font-size: 9.6px; line-height: 17.6px; color: var(--body-ink); margin-bottom: 2px; }
  .info__results { list-style: none; font-family: "Roboto Condensed", sans-serif; font-size: 9.6px; line-height: 16.4px; color: var(--body-ink); }
  .info__results li { position: relative; padding-left: 9px; }
  .info__results li::before { content: ""; position: absolute; left: 0; top: 6px; width: 5px; height: 5px; border-radius: 50%; background: var(--orchid); }
  .stamp-box { position: absolute; left: 476px; top: 14px; width: 58px; height: 65px; border: 1.5px solid var(--orchid); }
  .mailer { position: absolute; left: 330px; top: 135px; width: 180px; text-align: center; }
  .mailer__brand { display: flex; justify-content: center; align-items: center; gap: 7px;
    font-family: "Dancing Script", cursive; font-weight: 600; font-size: 24px; color: var(--leaf); margin-bottom: 16px; }
  .mailer__dot { width: 10px; height: 10px; border-radius: 50%; background: var(--leaf); }
  .contact { font-size: 11px; line-height: 15px; color: var(--body-ink); }
  .contact__name { font-family: "PT Sans", sans-serif; font-weight: 700; font-size: 14px; line-height: 18px; color: var(--orchid); }
  .contact__line { display: flex; justify-content: center; align-items: center; gap: 4px; }
  .contact__line svg { width: 9px; height: 9px; fill: var(--orchid); }
</style>
</head>
<body>

<section class="postcard postcard--front">
  <div class="front__photo" role="img" aria-label="Photo of a pregnant woman resting on her back in a green meadow"></div>
  <svg class="front__wave" width="558" height="433" viewBox="0 0 558 433" aria-hidden="true">
    <defs>
      <linearGradient id="bandFill" x1="0" y1="0" x2="1" y2="0.3">
        <stop offset="0" stop-color="#b768aa"/>
        <stop offset="0.5" stop-color="#b05ba4"/>
        <stop offset="1" stop-color="#c49ad3"/>
      </linearGradient>
    </defs>
    <path d="M0,312 C150,288 350,250 558,236 L558,433 L0,433 Z" fill="url(#bandFill)"/>
    <path d="M0,312 C150,288 350,250 558,236" fill="none" stroke="#ffffff" stroke-width="4"/>
    <path d="M0,318 C150,294 350,256 558,242" fill="none" stroke="#ecdaeb" stroke-width="2" opacity=".6"/>
  </svg>
  <p class="front__tagline">Healing the mind, body, spirit and soul with Energy provided to all living things by the Universe.</p>
  <div class="brand"><span class="brand__dot"></span>Harbor &amp; Fern</div>
  <div class="practitioner">
    <p class="practitioner__name">Clara M. Whitfield</p>
    <p class="practitioner__title">Reiki Master Teacher,</p>
    <p class="practitioner__title">Archangelic Light Master Teacher</p>
  </div>
  <ul class="benefits">
    <li>Deep Relaxation</li>
    <li>Decrease Anxiety</li>
    <li>Decrease Stress</li>
    <li>Decrease Discomforts</li>
    <li>Promote Feeling of Wellbeing</li>
    <li>Promote Balance</li>
    <li>Relieve Physical Discomforts of Pregnancy</li>
  </ul>
</section>

<section class="postcard postcard--back">
  <div class="back__wash"></div>
  <div class="info">
    <h2 class="info__heading">How Can Clara M. Whitfield help when you are pregnant</h2>
    <p class="info__text">The benefits of Reiki given to the pregnant woman are countless. Reiki therapy is a safe, non-invasive, holistic energy therapy for mothers to use throughout pregnancy, labor, and postpartum. Reiki can be useful for relieving many of the physical discomforts of pregnancy. It can help to reduce stress and calm the emotions that occur as a woman adjusts to the hormones and life changes associated with this time. Reiki can also provide a non-invasive comfort measure during labor, helping to relieve pain and reduce anxiety. Because of Reiki's relaxing nature, it can be particularly helpful for releasing any fears a woman has as she approaches her birthing time. In addition, treatment can be beneficial during the postpartum period by promoting the healing process of the body.</p>
    <p class="info__text">At Lakeside Hospital in Millbrook, Vermont, tests were conducted throughout pregnancy using only the simplest form of Reiki. What they found was that Reiki</p>
    <ul class="info__results">
      <li>Reduced stress &amp; anxiety in pregnancy by 94%</li>
      <li>Reduced pain by 78%</li>
      <li>Nausea &amp; morning sickness were reduced by 80%</li>
      <li>Quality of sleep was improved by 86%</li>
    </ul>
  </div>
  <div class="stamp-box" aria-label="Stamp area"></div>
  <div class="mailer">
    <div class="mailer__brand"><span class="mailer__dot"></span>Harbor &amp; Fern</div>
    <div class="contact">
      <p class="contact__name">CLARA M. WHITFIELD</p>
      <p>48 Willow Brook Ln.</p>
      <p>Millbrook, VT 05710</p>
      <p class="contact__line"><svg viewBox="0 0 10 10" aria-hidden="true"><circle cx="5" cy="5" r="5"/><path d="M3,2.5 L4.2,2.5 L4.6,4 L4,4.5 C4.4,5.3 4.8,5.7 5.5,6 L6,5.4 L7.5,5.8 L7.5,7 C5,7.2 2.8,5 3,2.5 Z" fill="#fff"/></svg>802.555.0147</p>
      <p class="contact__line"><svg viewBox="0 0 10 8" aria-hidden="true"><rect x="0" y="1" width="10" height="6.5" rx="1"/><path d="M0.5,1.5 L5,4.8 L9.5,1.5" fill="none" stroke="#fff" stroke-width="0.9"/></svg>clarawhitfield@mailbox.com</p>
    </div>
  </div>
</section>

</body>
</html>
```